PRP Poster

We need a poster for a doctors room to encourage people to enquire about PRP procedure.

It needs to include "for osteoarthritis and sports injuries" and "enhancing the body's natural ability to heal".

A brochure is attached which outlines what PRP (Platelet Rich Plasma) is, in the brochure it is called NTQ. DO NOT USE ANY OF THE LOGOS FROM THIS BROCHURE.

Target Market(s)

patients in an orthopaedic surgery waiting room/area
age range from teenagers till 80year olds
male= female ratio

Requirements
Must have
• single poster
eye-catching yet professional
needs to be suitable/appropriate for the waiting area of a surgeons clinic
Nice to have
• prp is a natural therapy (it is essentially the person's own blood being reinjected to a site of injury)
the "natural" aspect of the therapy needs to be emphasised

```html
<!DOCTYPE html>
<html lang="en">
<head>
<meta charset="utf-8">
<title>Platelet Rich Plasma Poster</title>
<link href="https://fonts.googleapis.com/css2?family=Anton&family=Open+Sans:wght@700&family=Roboto+Condensed:wght@700&display=swap" rel="stylesheet">
<style>
  :root {
    --poster-orange: #e2502a;
    --ink-black: #1d1b1a;
    --text-white: #ffffff;
    --golf-green: #6f9a3c;
    --golf-sky: #c9d6c2;
    --pitch-green: #5f8f3a;
    --pitch-light: #b9c9b4;
    --arc-glow: rgba(255,255,255,0.55);
  }
  html, body {
    margin: 0;
    padding: 0;
    overflow: hidden;
    background: #ffffff;
  }
  .poster {
    position: relative;
    width: 800px;
    height: 1200px;
    background: var(--poster-orange);
    overflow: hidden;
    font-family: "Open Sans", Arial, sans-serif;
  }
  .photo-frame {
    position: absolute;
    display: block;
  }
  .photo-frame--golf {
    left: 0;
    top: 0;
    width: 420px;
    height: 310px;
  }
  .photo-frame--football {
    left: 380px;
    top: 870px;
    width: 420px;
    height: 330px;
  }
  .indication {
    position: absolute;
    left: 345px;
    top: 150px;
    margin: 0;
    color: var(--text-white);
    font-weight: 700;
    line-height: 50px;
    font-size: 40px;
    letter-spacing: 0.5px;
    white-space: nowrap;
  }
  .indication__small {
    font-size: 28px;
  }
  .headline {
    position: absolute;
    left: 0;
    top: 0;
    width: 800px;
    margin: 0;
    font-family: "Anton", Impact, sans-serif;
    font-weight: 400;
    color: var(--ink-black);
  }
  .headline__line {
    position: absolute;
    left: 0;
    width: 800px;
    text-align: center;
    font-size: 136px;
    line-height: 136px;
    transform: scaleX(1.1);
    transform-origin: center;
    letter-spacing: 1px;
  }
  .headline__line--platelet { top: 378px; }
  .headline__line--rich { top: 518px; }
  .headline__line--plasma { top: 645px; }
  .tagline {
    position: absolute;
    left: 0;
    top: 766px;
    width: 800px;
    margin: 0;
    text-align: center;
    color: var(--text-white);
    font-family: "Roboto Condensed", "Arial Narrow", sans-serif;
    font-weight: 700;
    font-size: 47px;
    line-height: 54px;
    white-space: nowrap;
  }
  .quote {
    position: absolute;
    left: 28px;
    top: 896px;
    margin: 0;
    color: var(--text-white);
    font-family: "Roboto Condensed", "Arial Narrow", sans-serif;
    font-weight: 700;
    font-size: 49px;
    line-height: 50px;
    white-space: nowrap;
  }
</style>
</head>
<body>
<main class="poster">
  <svg class="photo-frame photo-frame--golf" viewBox="0 0 420 310" role="img" aria-label="Photograph of two golfers on a green course fairway, one mid-swing">
    <defs>
      <linearGradient id="golfScene" x1="0" y1="0" x2="0" y2="1">
        <stop offset="0" stop-color="var(--golf-sky)"/>
        <stop offset="0.35" stop-color="#5d7a4a"/>
        <stop offset="0.6" stop-color="var(--golf-green)"/>
        <stop offset="1" stop-color="#88b04a"/>
      </linearGradient>
    </defs>
    <path d="M0 0 H408 C390 140 260 270 0 302 Z" fill="url(#golfScene)"/>
    <path d="M408 0 C390 140 260 270 0 302" fill="none" stroke="var(--arc-glow)" stroke-width="12"/>
  </svg>

  <p class="indication">
    <span class="indication__small">FOR</span> ARTHRITIS<br>
    <span class="indication__small">AND</span> SPORTS INJURIES
  </p>

  <h1 class="headline">
    <span class="headline__line headline__line--platelet">PLATELET</span>
    <span class="headline__line headline__line--rich">RICH</span>
    <span class="headline__line headline__line--plasma">PLASMA</span>
  </h1>

  <p class="tagline">PRP is a Natural Therapy</p>

  <p class="quote">"Enhancing the Body's<br>Natural Ability to Heal"</p>

  <svg class="photo-frame photo-frame--football" viewBox="0 0 420 330" role="img" aria-label="Photograph of two women footballers contesting the ball on a grass pitch">
    <defs>
      <linearGradient id="pitchScene" x1="0" y1="0" x2="0" y2="1">
        <stop offset="0" stop-color="var(--pitch-light)"/>
        <stop offset="0.4" stop-color="#8aa57a"/>
        <stop offset="0.65" stop-color="var(--pitch-green)"/>
        <stop offset="1" stop-color="#6fa040"/>
      </linearGradient>
    </defs>
    <path d="M420 12 C230 50 60 170 16 330 H420 Z" fill="url(#pitchScene)"/>
    <path d="M420 12 C230 50 60 170 16 330" fill="none" stroke="var(--arc-glow)" stroke-width="12"/>
  </svg>
</main>
</body>
</html>
```